New Toothpaste brand needs a logo & packaging design

Our company is launching a new toothpaste and is looking for a logo and packaging design. The toothpaste brand is called Brivana. The packaging should have the same design quality as the major international brands, such as Lumora, Lumora Totalcare, Dentiva, Pexolo, Wind-rise, Marvest, etc. The dominant colors for our brand should be hues of blue, similar to other major brands. In addition, there should be a little bit of green to represent the "Fresh Mint Blast" flavor and the "Extracts of Aloe Vera" included in the ingredients.

There are typically 3 unique sides on a toothpaste box:

The face: Repeated on ~3 sides of the 4 faces of the box
The back: The 4th box face has the instructions for use, ingredients, company information, bar code/product info, and some branding elements.
The sides: Usually consisting of just the logo, flavor etc.

Please refer to existing brands such as Lumora, Lumora Total-care, and Dentiva for an example of typical box layout and elements.

Task Details:
Package Dimensions: 180 mm x 48 mm x 28 mm, 100 ml toothpaste tube
Brand Name: Brivana
Description: Fluoride Toothpaste
Flavor: Fresh Mint Blast
5 Actions: Protects against cavities and tartar, freshens breath, whitens teeth, and maintains healthy gums. These actions can also be made into a list like Lumora Total Care or Dentiva Max care. For instance, Strong Teeth, Fresh Breath, Whitening, Healthy Gums, Cavity and Tartar Protection.
Also contains whitening micro particles and extracts of aloe vera which may be highlighted on the package

Overall, the look should be high quality and with the same look and feel as the big brands mentioned previously. We do not have an existing logo for this brand. The face of the package is the most important element as it is often repeated on several sides and on the tube itself.

Please let me know if you have any questions.

I've attached some of our favorite big brand designs below. I would say the Lumora Total Care and Gleam vers

The logos I've seen so far for Brivana, have been a bit too bold. A little bold is okay, but just needs to be moderate. 

I would like the colors to be bright and appealing. I mentioned shades of blue being the major color, but green should also be highlighted as well, perhaps in a 80% blue to 20% green ratio. 

Target Market(s)

adult consumer of toothpaste, both female and male.

Industry/Entity Type

It Company

Requirements
Must have
• A logo with the brand name: Brivana
Description or sub text: Fluoride Toothpaste
Flavor: Fresh Mint Blast
A phrase or list describing the Toothpaste Actions: e.g., Protects against cavities and tartar, freshens breath, whitens teeth, and maintains healthy gums. Or as a list simialr to Lumora Total Care or Dentiva Max Care:
-Anti-cavity
-Anti-tartar
-Fresh breath
-Whitening
-Healthy Gums

Special ingredient of "whitening micro particles: and "extracts of aloe vera", which should also be highlighted.

The color should mostly be shades of blue, with only a little bit of green to accentuate the fresh mint blast flavor and aloe vera

Nice to have
• The design should really look good next to lumora total care, gleam pure, and dentiva max care. These are our favorite designs.
Should not have
• For aloe vera, there is no need to show the plant.

The Brivana logo shouldn't be too Bold. This should be appeal to all consumers, not just men.

```html
<!DOCTYPE html>
<html lang="en">
<head>
<meta charset="utf-8">
<title>Brivana – Fresh Mint Blast toothpaste box face</title>
<link rel="stylesheet" href="https://fonts.googleapis.com/css2?family=Archivo:ital,wght@0,400;0,600;0,700;0,800;1,400;1,700&display=swap">
<style>
  :root{
    --page:#ffffff;
    --blue-deep:#0f3f8c;
    --blue-mid:#0a78c8;
    --blue-bright:#12aee8;
    --navy:#1b2f6e;
    --green:#3bb54a;
    --green-light:#8cc63f;
    --green-dark:#1f7a2e;
    --white:#ffffff;
  }
  html,body{margin:0;padding:0;width:1200px;height:900px;overflow:hidden;background:var(--page);}
  .canvas{position:relative;width:1200px;height:900px;font-family:"Archivo",Arial,sans-serif;}
  .box-face{
    position:absolute;left:234px;top:294px;width:767px;height:204px;overflow:hidden;
    background:linear-gradient(180deg,var(--blue-deep) 0%,var(--blue-mid) 30%,var(--blue-bright) 52%,var(--blue-mid) 76%,var(--blue-deep) 100%);
  }
  .droplets{position:absolute;border-radius:50%;
    background:radial-gradient(ellipse at center,rgba(120,200,245,.45) 0%,rgba(40,140,215,.25) 55%,rgba(40,140,215,0) 75%);}
  .droplets--right{left:440px;top:30px;width:250px;height:170px;}
  .droplets--logo{left:120px;top:95px;width:140px;height:90px;}
  .new-corner{position:absolute;left:0;top:0;width:70px;height:70px;}
  .new-label{position:absolute;left:6px;top:14px;font-size:10px;font-weight:800;color:var(--navy);transform:rotate(-45deg);letter-spacing:.5px;}
  .ingredient-note{position:absolute;left:94px;top:48px;font-size:8.5px;color:var(--white);white-space:nowrap;}
  .ingredient-note em{font-weight:700;}
  .brand-name{position:absolute;left:80px;top:56px;font-size:80px;font-weight:800;color:var(--white);letter-spacing:-1px;line-height:1;}
  .flavor-tag{position:absolute;left:565px;top:113px;width:202px;height:43px;background:var(--green);
    box-shadow:0 2px 0 var(--green-dark);display:flex;align-items:center;}
  .flavor-tag svg{margin-left:13px;margin-right:8px;}
  .flavor-name{font-size:13px;font-weight:700;color:var(--white);}
  .benefits{position:absolute;left:81px;top:177px;display:flex;align-items:center;gap:4px;
    font-size:12px;font-weight:700;color:var(--white);letter-spacing:.8px;white-space:nowrap;}
  .benefit-dot{width:12px;height:12px;border-radius:50%;background:var(--green-light);display:inline-block;margin:0 2px 0 4px;}
  .volume{position:absolute;right:13px;top:180px;font-size:12px;font-style:italic;color:var(--white);}
</style>
</head>
<body>
<div class="canvas">
  <section class="box-face">
    <div class="droplets droplets--right" role="img" aria-label="Cluster of water droplets decoration"></div>
    <div class="droplets droplets--logo" role="img" aria-label="Water droplets behind the brand name"></div>

    <svg class="new-corner" viewBox="0 0 70 70" aria-hidden="true">
      <defs><linearGradient id="newGrad" x1="0" y1="1" x2="1" y2="0">
        <stop offset="0" stop-color="#8cc63f"/><stop offset="1" stop-color="#3bb54a"/></linearGradient></defs>
      <polygon points="0,0 70,0 0,70" fill="url(#newGrad)"/>
    </svg>
    <span class="new-label">NEW</span>

    <p class="ingredient-note" style="margin:0">Special ingredient of <em>Whitening Micro Particles</em> and <em>Extracts Of Aloe Vera</em></p>

    <h1 class="brand-name" style="margin:0">Brivana</h1>

    <div class="flavor-tag">
      <svg width="46" height="20" viewBox="0 0 46 20" aria-hidden="true">
        <path d="M2 18 C8 4 26 0 44 4 C38 14 22 20 2 18 Z" fill="#ffffff"/>
      </svg>
      <span class="flavor-name">Fresh Mint Blast</span>
    </div>

    <div class="benefits">
      <span>Anti-cavity</span><i class="benefit-dot"></i>
      <span>Anti-tartar</span><i class="benefit-dot"></i>
      <span>Fresh Breath</span><i class="benefit-dot"></i>
      <span>Whitening</span><i class="benefit-dot"></i>
      <span>Healthy Gums</span>
    </div>

    <span class="volume">100ml</span>
  </section>
</div>
</body>
</html>
```